Dr Maren Holt, Orthopaedic Hand Surgeon

I am an orthopaedic hand surgeon and need business cards that reflect the surgery I do. I operate on bones, ligaments, tendons, and soft tissues. I can do microsurgery (surgery under an operating microscope) - including connecting ends of cut nerves and arteries in the fingers together. As an orthopaedic surgeon, I also fix fractures and manage orthopaedic trauma in the rest of the body. I favour black as a colour, and have some pictures of hand X-rays that you can use in the design, if you think that would look good (feel free to crop).

Hi all. Thank you for all your submissions so far. Please note that I have updated my project brief. I would like to emphasise that use of the logos that I have provided is optional, and if used, I would very much prefer the logo not to dominate the card, but add to the overall aesthetic of the card. Warm regards, Maren

Target Market(s)

Referring medical practitioners, hand therapists, patients

Industry/Entity Type

Healthcare

Contact Information for Business Card

Dr Maren Holt
Orthopaedic Hand Surgeon
MBBS BSc (Med), MIntPH (Merit), GWELN (Ortho), MIvroE

Font styles to use
Serif

Colors

Designer to choose colors to be used in the design.

Requirements
Must have
• Space for:
• 2 addresses (a PO Box Address and a consulting suite address) - to be confirmed
• 1 phone number - to be confirmed
Nice to have
• Please choose one of the GWELN logos (I included 3 - colour, black reverse, and greyscale); if you include this in the design, IT SHOULD NOT DOMINATE THE CARD, but be smaller and more discreet.
• I have also attached the MIvroE logo (colour and greyscale); if you choose to include this in the design, IT SHOULD NOT DOMINATE THE CARD, but be smaller and more discreet.
• I would love to be able to update details on the card as time goes on, and thus would like to own the template for the card as well.
• Also I would love discussion with regard to any changes on the card, if I am not completely happy with the design, and would like to discuss things such as ease of printing, finish on the cards (matte, polish) etc.
Should not have
• I don't like the card to look too crowded

```html
<!DOCTYPE html>
<html lang="en">
<head>
<meta charset="utf-8">
<title>Dr Maren Holt – Business Card</title>
<link rel="stylesheet" href="https://fonts.googleapis.com/css2?family=Gelasio:wght@400&family=Open+Sans:wght@400&family=Questrial&display=swap">
<style>
  :root {
    --page: #e9e6e1;
    --card: #000000;
    --green: #1e7a3c;
    --green-deep: #145a2b;
    --green-bright: #2ecc62;
    --green-text: #23b85a;
    --white: #ffffff;
  }
  html, body {
    margin: 0;
    width: 1200px;
    height: 891px;
    overflow: hidden;
    background: var(--page);
  }
  .card {
    position: absolute;
    width: 550px;
    height: 314px;
    background: var(--card);
    overflow: hidden;
    box-shadow: 0 6px 18px rgba(0,0,0,0.25);
  }
  .card--front { left: 36px; top: 288px; }
  .card--back  { left: 614px; top: 288px; }

  .card__lines {
    position: absolute;
    inset: 0;
  }
  .xray-area {
    position: absolute;
    background: radial-gradient(ellipse at 50% 30%, var(--green) 0%, var(--green-deep) 55%, rgba(20,90,43,0) 100%);
  }
  .card--front .xray-area { left: 50px; top: 0; width: 150px; height: 130px; }
  .card--back  .xray-area { left: 384px; top: 0; width: 166px; height: 150px; }

  .identity {
    position: absolute;
    right: 46px;
    top: 118px;
    text-align: right;
  }
  .name {
    margin: 0 0 6px;
    font-family: "Gelasio", serif;
    font-weight: 400;
    font-size: 36px;
    line-height: 1.1;
    color: var(--white);
    white-space: nowrap;
  }
  .name__initial { color: var(--green-bright); }
  .title,
  .credentials {
    margin: 0 0 4px;
    font-family: "Open Sans", sans-serif;
    font-size: 11.5px;
    color: var(--green-text);
    white-space: nowrap;
  }
  .contact-list {
    position: absolute;
    left: 28px;
    top: 48px;
    margin: 0;
    padding: 0;
    list-style: none;
    font-family: "Questrial", sans-serif;
    font-size: 13.5px;
    letter-spacing: 1px;
    color: var(--green-text);
  }
  .contact-list li { margin-bottom: 16px; white-space: nowrap; }
</style>
</head>
<body>

<section class="card card--front" aria-label="Business card front">
  <div class="xray-area" role="img" aria-label="Green hand X-ray illustration reaching down from the top edge"></div>
  <svg class="card__lines" width="550" height="314" viewBox="0 0 550 314" aria-hidden="true">
    <polyline points="216,0 216,132 22,314" fill="none" stroke="var(--green)" stroke-width="1.4"/>
  </svg>
  <div class="identity">
    <h1 class="name">Dr <span class="name__initial">M</span>aren Holt</h1>
    <p class="title">Orthopaedic Hand Surgeon</p>
    <p class="credentials">MBBS BSc (Med), MIntPH (Merit), GWELN (Ortho), MIvroE</p>
  </div>
</section>

<section class="card card--back" aria-label="Business card back">
  <svg class="card__lines" width="550" height="314" viewBox="0 0 550 314" aria-hidden="true">
    <line x1="368" y1="22" x2="362" y2="300" stroke="var(--green)" stroke-width="1.2"/>
  </svg>
  <ul class="contact-list">
    <li>- 2 addresses</li>
    <li>- 1 phone number - to be confirmed</li>
  </ul>
  <div class="xray-area" role="img" aria-label="Green hand X-ray illustration reaching in from the top right corner"></div>
</section>

</body>
</html>
```